Commercial and Residential landscape Flyer design

we would like a flyer to advertise our new landscaping division for our company. Phone Number 5184620371
email pinecrestgroundworkservices@mailorbit.net
address 7 Marlow Court Schenectady New York 12419
The design is up to you. ill attach some sample flyers in the file section
Target Market(s)
Residential and commercial properties
Industry/Entity Type
Landscape
Font styles to use
Sans Serif
Colors
Designer to choose colors to be used in the design.
Requirements
Must have
- Services offered
- Spring Cleanups
- Mulch installation
- Mowing
- Tree and shrub Maintenance
- Fall Cleanups
- Fully Insured
- Free Estimates
Nice to have
- See word file Please double check all grammar and spelling
- Feel free to use anything in the word file. Its totally up to you. It all doesn't need to be on it . would like to stick with the color scheme of the logo
Should not have
- there are no should not haves. We just want to get the word out that we have a landscape division

```html
<!DOCTYPE html>
<html lang="en">
<head>
<meta charset="utf-8">
<title>Commercial and Residential Landscaping Flyer</title>
<link rel="stylesheet" href="https://fonts.googleapis.com/css2?family=Roboto:wght@500;700&display=swap">
<style>
  :root {
    --brand-blue: #3f86c8;
    --brand-blue-deep: #2f6fb3;
    --brand-blue-light: #7fb1e0;
    --services-blue: rgba(64, 122, 190, 0.82);
    --ink: #111111;
    --slate: #5a5a5a;
    --band-grey: #6d6d6d;
    --paper: #ffffff;
    --lawn-1: #6fae3a;
    --lawn-2: #3f7a2a;
    --bloom: #c95a7a;
  }
  * { box-sizing: border-box; margin: 0; padding: 0; }
  html, body { width: 720px; height: 1200px; overflow: hidden; background: var(--paper); }
  .flyer {
    position: relative; width: 720px; height: 1200px; overflow: hidden;
    background: var(--paper);
    font-family: "Roboto", Arial, sans-serif; color: var(--ink);
  }
  .flyer-shapes { position: absolute; inset: 0; }
  .headline {
    position: absolute; left: 280px; top: 38px;
    font-size: 31px; font-weight: 500; line-height: 1.12; color: var(--ink);
  }
  .services {
    position: absolute; left: 541px; top: 240px; color: var(--paper);
    font-size: 18px; font-weight: 500; list-style: none;
  }
  .services-title { font-size: 19px; font-weight: 700; margin-bottom: 18px; }
  .services li { line-height: 1.18; margin-bottom: 22px; }
  .services li.two-line { margin-bottom: 18px; }
  .tagline {
    position: absolute; left: 188px; width: 320px; top: 633px; text-align: center;
    font-size: 29px; font-weight: 700; line-height: 44px; white-space: nowrap;
  }
  .about {
    position: absolute; left: 52px; top: 736px; width: 372px;
    font-size: 13.4px; font-weight: 700; line-height: 15.6px;
  }
  .company-name {
    position: absolute; left: 460px; top: 748px; width: 190px; text-align: center;
    font-size: 22px; font-weight: 700; line-height: 1.15; color: var(--brand-blue);
  }
  .company-dot {
    display: block; width: 30px; height: 30px; border-radius: 50%;
    background: var(--brand-blue); margin: 0 auto 10px;
  }
  .contact { position: absolute; right: 22px; top: 990px; text-align: right; color: var(--brand-blue); font-style: normal; }
  .contact-title { font-size: 29px; font-weight: 500; color: var(--slate); margin-right: 13px; }
  .contact-line { display: flex; align-items: center; justify-content: flex-end; gap: 8px; font-weight: 500; }
  .contact-phone { font-size: 31px; margin-top: 8px; margin-right: 13px; }
  .contact-email { font-size: 21px; margin-top: 6px; margin-right: 6px; }
  .contact-address { font-size: 24px; margin-top: 6px; }
  .contact-line svg { flex: none; }
</style>
</head>
<body>
<main class="flyer">
  <svg class="flyer-shapes" width="720" height="1200" viewBox="0 0 720 1200">
    <defs>
      <linearGradient id="gardenTones" x1="0" y1="0" x2="1" y2="1">
        <stop offset="0" stop-color="#3d5a2a"/>
        <stop offset="0.35" stop-color="#c95a7a"/>
        <stop offset="0.55" stop-color="#3f7a2a"/>
        <stop offset="1" stop-color="#6fae3a"/>
      </linearGradient>
      <linearGradient id="houseTones" x1="0" y1="0" x2="0" y2="1">
        <stop offset="0" stop-color="#8f8a82"/>
        <stop offset="0.45" stop-color="#4c4c4c"/>
        <stop offset="0.75" stop-color="#5f9a35"/>
        <stop offset="1" stop-color="#7cb944"/>
      </linearGradient>
      <linearGradient id="sweepBlue" x1="0" y1="0" x2="1" y2="0">
        <stop offset="0" stop-color="#2f6fb3"/>
        <stop offset="1" stop-color="#7fb1e0"/>
      </linearGradient>
    </defs>

    <path class="garden-photo" role="img" aria-label="Photo of a landscaped garden with flower beds and a curving lawn path"
          d="M0 150 Q360 120 720 150 L720 760 L0 760 Z" fill="url(#gardenTones)"/>
    <path class="header-rule" d="M250 150 Q480 118 720 152" fill="none" stroke="#3f86c8" stroke-width="7"/>

    <circle class="services-panel" cx="665" cy="430" r="200" fill="rgba(64, 122, 190, 0.82)"/>

    <circle class="house-photo" role="img" aria-label="Photo of a stone house with a curved driveway and landscaped lawn"
            cx="122" cy="175" r="140" fill="url(#houseTones)" stroke="#ffffff" stroke-width="4"/>

    <path class="lower-field" d="M0 715 Q360 505 720 726 L720 1200 L0 1200 Z" fill="#ffffff"/>
    <path class="lower-rule" d="M0 715 Q360 505 720 726" fill="none" stroke="#6d6d6d" stroke-width="5"/>

    <path class="grey-band" d="M0 880 Q360 980 720 840 L720 860 Q360 1000 0 905 Z" fill="#6d6d6d"/>
    <path class="blue-sweep" d="M0 905 Q360 1000 720 860 L720 1200 L0 1200 Z" fill="url(#sweepBlue)"/>
    <path class="contact-field" d="M0 1120 Q380 975 720 948 L720 1200 L0 1200 Z" fill="#ffffff"/>
  </svg>

  <h1 class="headline">Commercial and<br>Residential Landscaping</h1>

  <ul class="services">
    <li class="services-title">Services Offered</li>
    <li>- Spring Cleanups</li>
    <li>- Mulch installation</li>
    <li>- Mowing</li>
    <li class="two-line">- Tree and shrub<br>&nbsp;Maintenance</li>
    <li>- Fall Cleanups</li>
    <li>- Fully Insured</li>
    <li>- Free Estimates</li>
  </ul>

  <h2 class="tagline">Beautify Your Yard<br>or Business</h2>

  <p class="about">We can help you with all phases of the landscaping process, from designing an interesting, cohesive layout to installation. In addition to planting trees, shrubs, and flowers, our services also include the design and installation of the following landscaping features: Gardens, including Terraced Gardens, Patios, Walkways, Retaining Walls, and Xeriscaping. In addition, we provide seeding and sodding services, and we can also implement rock and mulch beds.</p>

  <div class="company-name"><span class="company-dot"></span>Pinecrest Groundwork Services</div>

  <address class="contact">
    <div class="contact-title">Contact Us</div>
    <div class="contact-line contact-phone">
      <svg width="34" height="34" viewBox="0 0 24 24" aria-hidden="true"><path d="M6.6 2.5l3 3.2-1.8 2.6c1.2 2.6 3.2 4.6 5.8 5.9l2.6-1.8 3.2 3-1.9 3.6C10 18.6 5.2 13.8 3 6.4z" fill="none" stroke="#3f86c8" stroke-width="1.9" stroke-linejoin="round"/></svg>
      <span>(518) 462-0371</span>
    </div>
    <div class="contact-line contact-email">
      <svg width="34" height="24" viewBox="0 0 34 24" aria-hidden="true"><rect x="1.5" y="1.5" width="31" height="21" fill="none" stroke="#3f86c8" stroke-width="3"/><path d="M2 3l15 11L32 3" fill="none" stroke="#3f86c8" stroke-width="3"/></svg>
      <span>pinecrestgroundworkservices@mailorbit.net</span>
    </div>
    <div class="contact-line contact-address">
      <svg width="28" height="40" viewBox="0 0 28 40" aria-hidden="true"><path d="M14 1C6.8 1 1 6.6 1 13.6 1 23 14 39 14 39s13-16 13-25.4C27 6.6 21.2 1 14 1z" fill="#3f86c8"/><circle cx="14" cy="13.5" r="5" fill="#ffffff"/></svg>
      <span>7 Marlow Court, Schenectady, New York 12419</span>
    </div>
  </address>
</main>
</body>
</html>
```